Business Card

I need a business card that really pops for a potential customer or person who refers a personal injury lead. I want to highlight our office locations, but only address that needs to be on the card is my office's main address. I want a sleek, modern and minimalist design.

```html
<!DOCTYPE html>
<html lang="en">
<head>
<meta charset="utf-8">
<title>Northgate Injury Attorneys – Business Card</title>
<link rel="stylesheet" href="https://fonts.googleapis.com/css2?family=Open+Sans:wght@400;700&display=swap">
<style>
  :root {
    --backdrop: #1f1f1f;
    --charcoal: #383838;
    --ink: #2e2e2e;
    --paper: #ffffff;
  }
  * { box-sizing: border-box; margin: 0; padding: 0; }
  html, body {
    width: 1200px; height: 900px; overflow: hidden;
    background: var(--backdrop);
    font-family: "Open Sans", Arial, sans-serif;
  }
  .stage {
    width: 1200px; height: 900px;
    display: flex; flex-direction: column; align-items: center; justify-content: center;
    gap: 40px;
  }
  .card {
    position: relative;
    width: 665px; height: 380px;
    overflow: hidden;
    box-shadow: 0 10px 30px rgba(0,0,0,0.45);
  }

  /* Front */
  .card-front { background: var(--paper); color: var(--ink); }
  .front-wave { position: absolute; inset: 0; width: 100%; height: 100%; }
  .front-wave .band, .front-wave .swoosh { fill: var(--charcoal); }
  .front-brand {
    position: absolute; left: 36px; top: 22px;
    color: var(--paper); font-weight: 400; line-height: 1;
  }
  .front-brand .brand-main { display: block; font-size: 34px; letter-spacing: 7px; }
  .front-brand .brand-sub { display: block; font-size: 12px; letter-spacing: 7.5px; margin-top: 5px; }

  .holder {
    position: absolute; right: 52px; top: 208px; text-align: right;
  }
  .holder-name { font-size: 20px; font-weight: 700; letter-spacing: 0.5px; line-height: 1.2; }
  .holder-title { font-size: 15px; font-weight: 400; line-height: 1.3; }
  .holder-marker {
    position: absolute; right: 20px; top: 222px;
    width: 22px; height: 46px; background: var(--charcoal);
  }

  .address {
    position: absolute; left: 58px; top: 262px;
    font-size: 15px; line-height: 1.4;
  }

  .contacts {
    position: absolute; right: 28px; bottom: 22px;
    list-style: none; text-align: right;
    font-size: 15px; line-height: 1.45;
  }
  .contacts li { display: flex; align-items: center; justify-content: flex-end; gap: 8px; }
  .contacts svg { width: 13px; height: 13px; fill: var(--ink); flex: none; }

  /* Back */
  .card-back {
    background: var(--charcoal); color: var(--paper);
    display: flex; flex-direction: column; justify-content: center;
    padding-left: 62px; padding-right: 40px;
  }
  .back-brand { font-weight: 400; line-height: 1; white-space: nowrap; }
  .back-brand .brand-main { display: block; font-size: 68px; letter-spacing: 12px; }
  .back-brand .brand-sub { display: block; font-size: 24px; letter-spacing: 16px; margin-top: 14px; margin-left: -4px; }
</style>
</head>
<body>
<main class="stage">

  <section class="card card-front" aria-label="Card front">
    <svg class="front-wave" viewBox="0 0 665 380" preserveAspectRatio="none" aria-hidden="true">
      <path class="band" d="M0,0 H665 V40 C540,48 420,62 300,68 C190,73 80,95 0,160 Z"/>
      <path class="swoosh" d="M120,94 C300,102 480,76 665,60 L665,70 C480,90 300,110 120,94 Z"/>
    </svg>

    <div class="front-brand">
      <span class="brand-main">NORTHGATE</span>
      <span class="brand-sub">INJURY ATTORNEYS</span>
    </div>

    <div class="holder">
      <p class="holder-name">DANIEL HART</p>
      <p class="holder-title">Managing Director</p>
    </div>
    <div class="holder-marker"></div>

    <p class="address">Your address, City<br>State, Zip 1234</p>

    <ul class="contacts">
      <li>123 456 789
        <svg viewBox="0 0 24 24" aria-hidden="true"><path d="M6.6 10.8a15.1 15.1 0 0 0 6.6 6.6l2.2-2.2c.3-.3.7-.4 1-.2 1.1.4 2.3.6 3.6.6.6 0 1 .4 1 1V20c0 .6-.4 1-1 1A17 17 0 0 1 3 4c0-.6.4-1 1-1h3.5c.6 0 1 .4 1 1 0 1.3.2 2.5.6 3.6.1.3 0 .7-.2 1Z"/></svg>
      </li>
      <li>info@youremail.com
        <svg viewBox="0 0 24 24" aria-hidden="true"><path d="M2 5h20v14H2Z M2 5l10 8 10-8" fill="var(--ink)"/><path d="M3 6l9 7 9-7" fill="none" stroke="#fff" stroke-width="1.6"/></svg>
      </li>
      <li>www.yourwebsite.com
        <svg viewBox="0 0 24 24" aria-hidden="true"><circle cx="12" cy="12" r="10"/><path d="M2 12h20M12 2c3 3 3 17 0 20M12 2c-3 3-3 17 0 20" fill="none" stroke="#fff" stroke-width="1.4"/></svg>
      </li>
    </ul>
  </section>

  <section class="card card-back" aria-label="Card back">
    <div class="back-brand">
      <span class="brand-main">NORTHGATE</span>
      <span class="brand-sub">INJURY ATTORNEYS</span>
    </div>
  </section>

</main>
</body>
</html>
```